依頼詳細
ご利用者様は農家の皆様で、ご年配の方が多いと思います。
農薬散布代行についての内容は決まっていますが、
細かなルールなどが決まっていませんので一緒に考えていきたいです。
記載項目
単価は、1反2200円税込10反より少ない場合でも最低10反価格になります。
往復100Km以上離れる場合は、10Km当たり150円の交通費をいただきます。
※薬剤はご準備ください。
サイズ
A4
ページ数
両面
希望イメージ
シンプル 複雑
単色 カラフル
暗い 明るい
日常 高級
遊び心 厳粛
未来的 伝統的
女性的 男性的
希望する色
水色系
納品ファイル
• 高解像度JPG (.jpg)
• イラストレーター形式 (.ai)
• フォトショップ形式 (.psd)
• PNG形式 (.png)
補足説明
まだ何もでき上ってません。
記載に必要な事項はご質問ください。
https://tomevo.work/hpsekusyonn/sannpudaikou/
■ 選んだ理由

分かりやすいデザインとイラストなどの素材。

■ 提案者全員のお礼・コメント

多くの提案ありがとうございます。
どれも素晴らしいもので感心しています。

```html
<!DOCTYPE html>
<html lang="ja">
<head>
<meta charset="utf-8">
<title>ドローンによる農薬散布代行</title>
<link href="https://fonts.googleapis.com/css2?family=Noto+Sans+JP:wght@400;500;700;900&display=swap" rel="stylesheet">
<style>
:root{
  --navy:#1b2f6b;
  --blue:#1f6fc0;
  --sky:#3aa0dc;
  --pale:#e8f4fb;
  --red:#e0304a;
  --orange:#ef8a1f;
  --green:#49a641;
  --text:#333;
  --white:#fff;
}
*{box-sizing:border-box;margin:0;padding:0}
html,body{width:849px;height:1200px;overflow:hidden;background:#fff}
body{font-family:"Noto Sans JP",sans-serif;color:var(--text)}
.flyer{position:relative;width:849px;height:1200px;overflow:hidden;background:#fff}
.top-bar{height:40px;background:var(--navy);color:var(--white);font-weight:700;font-size:19px;display:flex;align-items:center;justify-content:center;letter-spacing:1px}
.hero{position:relative;height:520px}
.hero-photo{position:absolute;inset:0;background:linear-gradient(180deg,#6fb4e3 0%,#a9d6f1 28%,#dbeef7 40%,#9cbf6a 52%,#6f9a3e 72%,#4d7a2c 100%)}
.lead-tag{position:absolute;left:38px;top:28px;background:var(--blue);color:#fff;font-weight:700;font-size:15px;padding:4px 12px;transform:rotate(-8deg)}
.lead-big{position:absolute;left:30px;top:60px;background:#fff;padding:2px 16px 6px;transform:rotate(-8deg);box-shadow:0 3px 8px rgba(0,0,0,.2)}
.lead-big b{font-size:58px;font-weight:900;color:var(--red);letter-spacing:2px}
.lead-big span{font-size:30px;font-weight:900;color:var(--red)}
.cloud{position:absolute;left:80px;top:190px;width:690px;height:160px}
.headline{position:absolute;left:0;right:0;top:200px;text-align:center}
.headline .sub{display:inline-block;background:var(--sky);color:#fff;font-weight:900;font-size:30px;padding:2px 22px;letter-spacing:2px}
.headline .main{display:block;margin-top:6px;font-size:56px;font-weight:900;color:var(--blue);letter-spacing:3px}
.headline .main small{font-size:44px}
.merits{position:absolute;left:0;right:0;top:368px;display:flex;justify-content:center;gap:34px}
.merit{width:160px;height:100px;border-radius:12px;border:3px solid #fff;color:#fff;font-weight:700;font-size:18px;line-height:1.4;display:flex;align-items:center;justify-content:center;text-align:center;box-shadow:0 3px 6px rgba(0,0,0,.25)}
.merit.orange{background:var(--orange)}
.merit.green{background:var(--green)}
.merit.blue{background:var(--sky)}
.intro{padding:18px 58px 0;font-size:13.5px;line-height:1.75;color:#222}
.info-row{display:flex;gap:20px;padding:16px 40px 0}
.recommend{flex:1.45;border:2px solid var(--sky);border-radius:8px;padding:10px 16px}
.box-title{font-weight:700;font-size:14px;color:var(--navy);margin-bottom:6px}
.recommend li{list-style:none;font-size:15px;font-weight:700;color:var(--navy);margin:6px 0;display:flex;align-items:center;gap:8px}
.recommend li::before{content:"";width:12px;height:12px;border-radius:50%;background:var(--green);flex:none}
.recommend .note{font-size:10px;color:#555;margin-top:6px;line-height:1.5}
.price{flex:1;border:2px solid var(--sky);border-radius:8px;padding:10px 16px;background:var(--pale)}
.price p{font-size:13.5px;margin:4px 0}
.price .unit{font-size:13px}
.price .total{font-size:30px;font-weight:900;color:var(--red)}
.price .total small{font-size:14px;color:var(--text);font-weight:500}
.service{display:flex;gap:18px;margin:20px 40px 0;padding-top:14px;border-top:2px solid var(--sky)}
.service-text{flex:1.5;min-width:0}
.service-text .s1{font-size:13px;color:var(--blue);font-weight:700}
.service-text .s2{font-size:17px;color:var(--navy);font-weight:900;margin:6px 0 8px;white-space:nowrap}
.service-text ul{list-style:none;font-size:10.5px;line-height:1.7;color:#444}
.service-photo{flex:1;height:130px;border-radius:6px;background:linear-gradient(160deg,#d9eef9,#8fa8b8 60%,#5b6b74)}
.footer{position:absolute;left:0;right:0;bottom:0;height:118px;background:var(--pale);display:flex;align-items:center;justify-content:space-between;padding:0 40px;border-top:4px solid var(--sky)}
.brand{display:flex;align-items:center;gap:10px;font-size:26px;font-weight:700;color:var(--navy)}
.brand i{width:18px;height:18px;border-radius:50%;background:var(--sky);display:block}
.brand small{display:block;font-size:13px;font-weight:500}
.contact{text-align:right}
.tel{display:flex;align-items:center;justify-content:flex-end;gap:8px;font-size:40px;font-weight:900;color:var(--blue);letter-spacing:1px}
.contact .addr{font-size:11px;color:#444;line-height:1.6}
</style>
</head>
<body>
<div class="flyer">
  <div class="top-bar">ドローンによる農業散布に興味はありませんか？!</div>

  <section class="hero">
    <div class="hero-photo" role="img" aria-label="青空の下、田園の上を飛ぶ農薬散布用ドローンの写真"></div>
    <div class="lead-tag">農家の皆様へ</div>
    <div class="lead-big"><b>朗報</b><span>です</span></div>
    <svg class="cloud" viewBox="0 0 690 160" aria-hidden="true">
      <path d="M40 150 Q0 150 10 110 Q20 80 60 88 Q70 40 120 50 Q150 10 210 30 Q250 0 300 22 Q350 0 400 24 Q450 4 490 32 Q550 16 580 56 Q630 50 640 90 Q690 100 675 140 Q670 150 650 150 Z" fill="#fff"/>
    </svg>
    <div class="headline">
      <span class="sub">ドローンによる</span>
      <span class="main">農薬散布代行<small>承ります!</small></span>
    </div>
    <div class="merits">
      <div class="merit orange">労働負担が<br>軽減される</div>
      <div class="merit green">作業時間を<br>短縮できる</div>
      <div class="merit blue">散布者の<br>安全性の向上</div>
    </div>
  </section>

  <p class="intro">農薬や肥料の散布を生産者様が行う場合、動力噴霧器を背負っての散布となり、散布面積が広い場合や、夏の暑い時期にもなると真夏の外作業はとてもつらい作業となります。また、作物を扱うため、きちんと散布しなければならないので技術も必要です。<br>ドローンでの農薬散布であれば、地上から操作するだけで農薬を空中から散布することができるので、生産者様の労働負担は大幅に軽減されます。</p>

  <div class="info-row">
    <div class="recommend">
      <div class="box-title">こんな方におすすめ!</div>
      <ul>
        <li>ドローンに興味があるが、購入するには気が引ける。</li>
        <li>高齢化で農作業が困難になってきた。</li>
        <li>自分でできるがやはり作業代行を依頼したい。</li>
      </ul>
      <p class="note">※薬剤はご準備ください。往復100km以上離れる場合は10km当たり150円の交通費をいただきます。</p>
    </div>
    <div class="price">
      <div class="box-title">〈料金〉</div>
      <p>● 数量制限：10反より～</p>
      <p class="unit">1反：2,200円（税込）× 10反</p>
      <p class="total">22,000円<small>（税込）</small></p>
    </div>
  </div>

  <div class="service">
    <div class="service-text">
      <p class="s1">ドローンメーカーから出来る多くの機体に対応！</p>
      <p class="s2">ドローンの販売、メンテナンスや出張指導も可能です。</p>
      <ul>
        <li>主力販売機種：農業用ドローン各種、空撮用ドローン各種</li>
        <li>・点検、修理、バッテリー交換にも対応いたします</li>
        <li>・操縦講習や出張での使い方指導も承ります</li>
      </ul>
    </div>
    <div class="service-photo" role="img" aria-label="着陸した農業用ドローン機体の写真"></div>
  </div>

  <footer class="footer">
    <div class="brand"><i></i><div><small>ドローンショップ</small>ソラノワ</div></div>
    <div class="contact">
      <div class="tel">
        <svg width="34" height="34" viewBox="0 0 24 24" aria-hidden="true"><path fill="#1f6fc0" d="M6.6 10.8a15 15 0 0 0 6.6 6.6l2.2-2.2c.3-.3.7-.4 1-.2 1.1.4 2.3.6 3.6.6.6 0 1 .4 1 1V20c0 .6-.4 1-1 1A17 17 0 0 1 3 4c0-.6.4-1 1-1h3.5c.6 0 1 .4 1 1 0 1.3.2 2.5.6 3.6.1.3 0 .7-.2 1z"/></svg>
        093-555-0148
      </div>
      <p class="addr">〒800-0000 福岡県みなと市港町1丁目2-3<br>https://tomevo.work/</p>
    </div>
  </footer>
</div>
</body>
</html>
```